Modern Quillby Tree Care Website

I need a website for a full service Tree Care company. The company provides tree pruning, tree removal, tree preservation, emergency services, stump grinding, and emergency tree services.

Target Market(s)

Customers that need tree services

Industry/Entity Type

Landscaping, Tree Services

Coding

Coded - Design and coding required

Number of Pages Required

5+ page

Font styles to use
Sans Serif

Requirements
Must have
• Good clean design that showcases the services the company provides.
Nice to have
• Services page; contact form, blog, home page, about page

```html
<!DOCTYPE html>
<html lang="en">
<head>
<meta charset="UTF-8">
<title>Quillby Tree Care</title>
<link href="https://fonts.googleapis.com/css2?family=Poppins:wght@400;500;600;700;800&display=swap" rel="stylesheet">
<style>
:root{
  --green:#7cc142;
  --green-dark:#5fa12c;
  --orange:#f5a623;
  --ink:#545454;
  --text:#666;
  --light:#f3f3f3;
  --footer:#10180e;
  --white:#fff;
}
*{box-sizing:border-box;margin:0;padding:0}
html,body{width:1200px;height:5199px;overflow:hidden}
body{position:relative;font-family:'Poppins',sans-serif;color:var(--text);background:var(--white)}
.abs{position:absolute}
.ph{position:absolute}
/* buttons */
.btn{position:absolute;height:50px;background:var(--green);color:#fff;font-weight:700;font-size:13px;
  display:flex;align-items:center;justify-content:center;gap:8px;letter-spacing:.3px}
.btn::after{content:"";position:absolute;right:-12px;top:0;width:24px;height:100%;
  background:var(--orange);clip-path:polygon(0 0,100% 0,55% 100%,0 100%)}
.btn.orange{background:var(--orange)}
.btn.orange::after{background:var(--orange);clip-path:polygon(30% 0,100% 0,60% 100%,0 100%);right:-14px;border-left:3px solid #fff}
.arrow{width:14px;height:14px;border-radius:50%;background:#fff;display:inline-flex;align-items:center;justify-content:center}
.arrow svg{width:8px;height:8px}
/* header */
.topbar{left:630px;top:0;width:570px;height:46px;background:var(--green);clip-path:polygon(4% 0,100% 0,100% 100%,0 100%)}
.topbar .ph-item{position:absolute;top:12px;color:#fff;font-size:15px;display:flex;align-items:center;gap:12px}
.ph-icon{width:26px;height:26px;border:2px solid currentColor;border-radius:50%;display:inline-flex;align-items:center;justify-content:center}
.ph-icon svg{width:12px;height:12px}
.brand{display:flex;align-items:center;gap:12px}
.brand-mark{width:52px;height:52px;background:var(--green)}
.brand-name{font-weight:700;font-size:26px;line-height:1.05;color:var(--ink);letter-spacing:1px}
.nav{left:450px;top:74px;display:flex;gap:38px;font-size:14px;color:var(--ink);text-transform:uppercase}
.nav a{color:inherit;text-decoration:none;position:relative}
.nav a.active{color:var(--orange)}
.nav a.active::after{content:"";position:absolute;left:0;right:0;bottom:-10px;height:2px;background:var(--orange)}
.social{display:flex;gap:10px}
.social span{width:44px;height:44px;border:2px solid var(--ink);border-radius:50%;display:block}
/* hero */
.hero{left:0;top:118px;width:1200px;height:637px;background:linear-gradient(120deg,#e9e8e3,#dcd9d0 60%,#d2cec4)}
.tag{left:120px;top:290px;height:36px;padding:0 38px 0 36px;background:var(--green);color:#fff;font-weight:700;font-size:19px;display:flex;align-items:center;
  clip-path:polygon(3% 0,100% 0,94% 100%,0 100%)}
.hero h1{left:120px;top:332px;font-size:60px;font-weight:800;color:var(--ink);line-height:66px;letter-spacing:.5px}
.hero-sub{left:120px;top:480px;font-size:15px;font-weight:500;color:var(--ink);letter-spacing:.6px}
.dots{left:568px;top:712px;display:flex;gap:14px}
.dots i{width:8px;height:8px;border-radius:50%;background:#fff;display:block}
.dots i.on{background:var(--green);width:10px;height:10px;margin-top:-1px}
/* section titles */
.sec-title{position:absolute;left:0;width:1200px;text-align:center;font-weight:800;font-size:44px;color:var(--ink)}
.sec-sub{position:absolute;left:0;width:1200px;text-align:center;font-size:15px;color:var(--green);letter-spacing:9px;font-weight:500}
.sec-line{position:absolute;left:572px;width:56px;height:3px;background:var(--orange)}
/* services */
.card{position:absolute;width:308px;height:366px;border:2px solid #ddd;background:#fff;text-align:center}
.card .img{position:absolute;left:12px;top:12px;right:12px;height:172px}
.card h3{position:absolute;top:212px;left:0;right:0;font-size:17px;font-weight:700;color:var(--ink)}
.card h3::after{content:"";display:block;width:40px;height:3px;background:var(--orange);margin:10px auto 0}
.card p{position:absolute;top:250px;left:20px;right:20px;font-size:15px;line-height:28px;color:var(--text)}
.card .more{position:absolute;top:316px;left:0;right:0;font-size:13px;font-weight:700;color:var(--green);display:flex;justify-content:center;align-items:center;gap:8px}
.more .arrow{background:var(--green)}
/* about */
.about-green{left:0;top:1911px;width:1200px;height:625px;background:linear-gradient(90deg,#6cb232,#7fc243)}
.about-photo{left:0;top:1911px;width:630px;height:625px;background:linear-gradient(140deg,#3f5a28,#6c7a3e 45%,#c68327 70%,#2f3b22);
  clip-path:polygon(0 0,630px 0,410px 625px,0 625px)}
.about h2{left:630px;top:2010px;font-size:44px;font-weight:800;color:#fff}
.about .small{left:630px;top:2070px;font-size:15px;color:#fff;letter-spacing:9px;font-weight:500}
.about p{left:630px;top:2125px;width:450px;color:#fff;font-size:15px;line-height:27.5px}
/* why */
.why-item{position:absolute;width:124px;height:124px;border-radius:50%;background:#fff;box-shadow:0 6px 12px rgba(0,0,0,.12);display:flex;align-items:center;justify-content:center}
.why-item::before{content:"";position:absolute;inset:0;border-radius:50%;border:4px solid var(--orange);clip-path:inset(0 0 0 50%)}
.why-item.g::before{border-color:var(--green)}
.why-item.l::before{clip-path:inset(0 50% 0 0)}
.why-item .ic{width:46px;height:46px;border-radius:8px;background:var(--orange)}
.why-item.g .ic{background:var(--green)}
.why-label{position:absolute;font-size:14px;font-weight:600;color:var(--ink);line-height:26px;text-transform:uppercase}
.why-label.r{text-align:right}
/* contact */
.contact-band{left:0;top:3272px;width:1200px;height:448px;background:linear-gradient(120deg,#f3a41f,#f7b13a 50%,#f19a1a)}
.contact-card{left:120px;top:3500px;width:958px;height:435px;background:#fff;box-shadow:0 6px 30px rgba(0,0,0,.08)}
.field{position:absolute;background:var(--light);font-size:13px;color:#999;padding:18px 20px;letter-spacing:.3px}
.cphone{position:absolute;display:flex;align-items:center;gap:14px;color:var(--orange);font-size:15px}
/* news */
.post-img{position:absolute;top:4153px;width:312px;height:235px}
.post-title{position:absolute;top:4420px;width:320px;font-size:17px;font-weight:700;color:var(--ink);line-height:27px}
.post-meta{position:absolute;top:4492px;font-size:13px;color:var(--text);display:flex;gap:16px;align-items:center}
.post-meta b{display:inline-block;width:11px;height:11px;background:var(--orange);border-radius:2px;margin-right:6px;vertical-align:-1px}
/* footer */
.footer{left:0;top:4690px;width:1200px;height:509px;background:var(--footer)}
.f-head{position:absolute;top:4787px;color:var(--orange);font-weight:700;font-size:17px}
.f-list{position:absolute;top:4835px;color:#fff;font-size:15px;line-height:41.5px;list-style:none}
.f-contact{position:absolute;left:810px;color:#fff;font-size:15px;line-height:25px;display:flex;gap:22px;align-items:flex-start}
.f-pin{width:44px;height:44px;border-radius:50%;background:var(--orange);flex:none;display:flex;align-items:center;justify-content:center}
.f-pin svg{width:18px;height:18px}
.footer-social span{border-color:#777}
</style>
</head>
<body>

<!-- header -->
<div class="abs topbar">
  <div class="ph-item" style="left:52px"><span class="ph-icon"><svg viewBox="0 0 24 24"><path fill="#fff" d="M6.6 10.8a15 15 0 006.6 6.6l2.2-2.2a1 1 0 011-.25 11.4 11.4 0 003.6.57 1 1 0 011 1V20a1 1 0 01-1 1A17 17 0 013 4a1 1 0 011-1h3.5a1 1 0 011 1c0 1.25.2 2.45.57 3.6a1 1 0 01-.25 1z"/></svg></span>(555) 014-2739</div>
  <div class="ph-item" style="left:240px;color:#e8f5dc">|</div>
  <div class="ph-item" style="left:275px"><span class="ph-icon"><svg viewBox="0 0 24 24"><path fill="#fff" d="M6.6 10.8a15 15 0 006.6 6.6l2.2-2.2a1 1 0 011-.25 11.4 11.4 0 003.6.57 1 1 0 011 1V20a1 1 0 01-1 1A17 17 0 013 4a1 1 0 011-1h3.5a1 1 0 011 1c0 1.25.2 2.45.57 3.6a1 1 0 01-.25 1z"/></svg></span>(555) 019-9939</div>
</div>
<div class="abs brand" style="left:120px;top:32px">
  <span class="brand-mark"></span>
  <span class="brand-name">QUILLBY<br>TREE CARE</span>
</div>
<nav class="abs nav">
  <a class="active">Home</a><a>About</a><a>Services</a><a>Blog</a><a>Contact</a>
</nav>
<div class="abs social" style="left:920px;top:61px"><span></span><span></span><span></span></div>

<!-- hero -->
<section class="abs hero" role="img" aria-label="Soft background of cut logs in a forest"></section>
<div class="abs tag">CALL QUILLBY FOR</div>
<h1 class="abs" style="left:120px;top:332px;font-size:60px;font-weight:800;color:var(--ink);line-height:66px">ALL YOUR TREE<br>CARE NEEDS.</h1>
<div class="abs hero-sub">SERVING MAPLE RIDGE AND SURROUNDING AREAS</div>
<div class="btn orange" style="left:120px;top:530px;width:212px">GET FREE ESTIMATE <span class="arrow"><svg viewBox="0 0 10 10"><path d="M3 2l3 3-3 3" stroke="#f5a623" stroke-width="2" fill="none"/></svg></span></div>
<div class="ph" style="left:636px;top:215px;width:442px;height:443px;background:linear-gradient(150deg,#5c6b3c,#8a7a55 45%,#c8512a 75%,#3b3a2c)" role="img" aria-label="Arborist cutting a log with a chainsaw"></div>
<div class="abs dots"><i></i><i class="on"></i><i></i></div>

<!-- services -->
<h2 class="sec-title" style="top:833px">OUR SERVICES</h2>
<div class="sec-sub" style="top:894px">WHAT WE DO</div>
<div class="sec-line" style="top:922px"></div>

<div class="card" style="left:120px;top:978px"><div class="img" style="background:linear-gradient(135deg,#6f8a4a,#b8582c 55%,#38452a)" role="img" aria-label="Worker trimming a hedge"></div><h3>TREE TRIMMING</h3><p>Incididunt ut labore et dolore maga aliqua ut enim ado.</p><div class="more">VIEW MORE <span class="arrow"><svg viewBox="0 0 10 10"><path d="M3 2l3 3-3 3" stroke="#fff" stroke-width="2" fill="none"/></svg></span></div></div>
<div class="card" style="left:445px;top:978px"><div class="img" style="background:linear-gradient(160deg,#9fc0d8,#7a9a4e 50%,#a08763)" role="img" aria-label="Climber removing a tree"></div><h3>TREE REMOVAL</h3><p>Incididunt ut labore et dolore maga aliqua ut enim ado.</p><div class="more">VIEW MORE <span class="arrow"><svg viewBox="0 0 10 10"><path d="M3 2l3 3-3 3" stroke="#fff" stroke-width="2" fill="none"/></svg></span></div></div>
<div class="card" style="left:771px;top:978px"><div class="img" style="background:linear-gradient(140deg,#5d5a45,#c0462a 55%,#4c5533)" role="img" aria-label="Machine clearing fallen trees"></div><h3>TREE CLEARING</h3><p>Incididunt ut labore et dolore maga aliqua ut enim ado.</p><div class="more">VIEW MORE <span class="arrow"><svg viewBox="0 0 10 10"><path d="M3 2l3 3-3 3" stroke="#fff" stroke-width="2" fill="none"/></svg></span></div></div>
<div class="card" style="left:120px;top:1363px"><div class="img" style="background:linear-gradient(135deg,#3f5a2a,#c8a06a 50%,#2d3a20)" role="img" aria-label="Chainsaw beside a cut log"></div><h3>TREE PRUNING</h3><p>Incididunt ut labore et dolore maga aliqua ut enim ado.</p><div class="more">VIEW MORE <span class="arrow"><svg viewBox="0 0 10 10"><path d="M3 2l3 3-3 3" stroke="#fff" stroke-width="2" fill="none"/></svg></span></div></div>
<div class="card" style="left:445px;top:1363px"><div class="img" style="background:linear-gradient(135deg,#6a5f43,#3f6a3a 50%,#4a3d2a)" role="img" aria-label="Stump grinding machine"></div><h3>STUMP GRINDING</h3><p>Incididunt ut labore et dolore maga aliqua ut enim ado.</p><div class="more">VIEW MORE <span class="arrow"><svg viewBox="0 0 10 10"><path d="M3 2l3 3-3 3" stroke="#fff" stroke-width="2" fill="none"/></svg></span></div></div>
<div class="card" style="left:771px;top:1363px"><div class="img" style="background:linear-gradient(135deg,#4e6a3a,#8c8a6c 50%,#3c4a2e)" role="img" aria-label="Old oak tree with wide branches"></div><h3>TREE PRESERVATION</h3><p>Incididunt ut labore et dolore maga aliqua ut enim ado.</p><div class="more">VIEW MORE <span class="arrow"><svg viewBox="0 0 10 10"><path d="M3 2l3 3-3 3" stroke="#fff" stroke-width="2" fill="none"/></svg></span></div></div>

<div class="btn" style="left:514px;top:1765px;width:160px">VIEW MORE <span class="arrow"><svg viewBox="0 0 10 10"><path d="M3 2l3 3-3 3" stroke="#7cc142" stroke-width="2" fill="none"/></svg></span></div>

<!-- about -->
<section class="about">
  <div class="abs about-green"></div>
  <div class="abs about-photo" role="img" aria-label="Arborist in safety gear looking up at a tree trunk"></div>
  <h2 class="abs">ABOUT QUILLBY</h2>
  <div class="abs small">TREE CARE</div>
  <p class="abs">At Quillby Tree Care, we are more than just a tree service company, we are stewards of our beautiful trees. With a passion deeply rooted in arboriculture, we embark on a mission to promote the health, beauty, and safety of your trees and landscapes. Whether it's expert tree trimming to enhance aesthetics, meticulous tree removal to mitigate hazards, or comprehensive tree health assessments to ensure safety...</p>
  <div class="btn" style="left:630px;top:2372px;width:160px;background:#8fcc55">VIEW MORE <span class="arrow"><svg viewBox="0 0 10 10"><path d="M3 2l3 3-3 3" stroke="#8fcc55" stroke-width="2" fill="none"/></svg></span></div>
</section>

<!-- why choose us -->
<h2 class="sec-title" style="top:2616px">WHY CHOOSE US</h2>
<div class="sec-sub" style="top:2677px">WHAT OUR DIFFERENT</div>
<div class="sec-line" style="top:2706px"></div>

<svg class="abs" style="left:0;top:2800px" width="1200" height="360" viewBox="0 2800 1200 360">
  <circle cx="600" cy="2975" r="122" fill="none" stroke="#ccc" stroke-width="4"/>
  <circle cx="600" cy="2975" r="106" fill="#fff" stroke="#d4a55c" stroke-width="4"/>
  <g fill="none" stroke-width="4" stroke-linecap="round">
    <path d="M440 2855c25 14 40 12 60 6" stroke="#d4a55c"/>
    <path d="M462 2895c10-12 20-18 34-16" stroke="#d4a55c"/>
    <path d="M380 2962c30-8 55-10 80-2" stroke="#7cc142"/>
    <path d="M380 2988c30 8 55 10 80 2" stroke="#7cc142"/>
    <path d="M440 3095c25-14 40-12 60-6" stroke="#f5a623"/>
    <path d="M462 3055c10 12 20 18 34 16" stroke="#f5a623"/>
    <path d="M760 2855c-25 14-40 12-60 6" stroke="#d4a55c"/>
    <path d="M738 2895c-10-12-20-18-34-16" stroke="#d4a55c"/>
    <path d="M820 2962c-30-8-55-10-80-2" stroke="#7cc142"/>
    <path d="M820 2988c-30 8-55 10-80 2" stroke="#7cc142"/>
    <path d="M760 3095c-25-14-40-12-60-6" stroke="#f5a623"/>
    <path d="M738 3055c-10 12-20 18-34 16" stroke="#f5a623"/>
  </g>
  <rect x="550" y="2925" width="100" height="100" rx="10" fill="#7cc142"/>
</svg>

<div class="why-item l" style="left:310px;top:2768px"><span class="ic"></span></div>
<div class="why-item g l" style="left:253px;top:2913px"><span class="ic"></span></div>
<div class="why-item l" style="left:310px;top:3056px"><span class="ic"></span></div>
<div class="why-item" style="left:763px;top:2768px"><span class="ic"></span></div>
<div class="why-item g" style="left:823px;top:2913px"><span class="ic"></span></div>
<div class="why-item" style="left:763px;top:3056px"><span class="ic"></span></div>

<div class="why-label r" style="left:100px;width:196px;top:2798px">Licensed and<br>insured</div>
<div class="why-label r" style="left:40px;width:196px;top:2943px">Highly<br>pro work</div>
<div class="why-label r" style="left:80px;width:216px;top:3086px">Licensed<br>arborist on staff</div>
<div class="why-label" style="left:902px;top:2798px">Locally owned<br>&amp; operated</div>
<div class="why-label" style="left:962px;top:2943px">Free<br>estimate</div>
<div class="why-label" style="left:902px;top:3086px">Safety is our no.1<br>priority</div>

<!-- contact -->
<div class="abs contact-band" role="img" aria-label="Warm orange wash over a chainsaw cutting wood"></div>
<h2 class="sec-title" style="top:3355px;color:#fff">CONTACT US</h2>
<div class="sec-sub" style="top:3414px;color:#fff">GET IN TOUCH</div>
<div class="sec-line" style="top:3442px;background:#fff"></div>
<div class="abs contact-card"></div>
<div class="ph" style="left:148px;top:3528px;width:304px;height:377px;background:linear-gradient(150deg,#8a6f4c,#d46a2a 40%,#a58a5e 65%,#6f5a3c)" role="img" aria-label="Chainsaw cutting through a log"></div>
<div class="field" style="left:482px;top:3528px;width:276px;height:52px">NAME</div>
<div class="field" style="left:774px;top:3528px;width:276px;height:52px">EMAIL</div>
<div class="field" style="left:482px;top:3597px;width:276px;height:52px">PHONE</div>
<div class="field" style="left:774px;top:3597px;width:276px;height:52px">SUBJECT</div>
<div class="field" style="left:482px;top:3667px;width:568px;height:161px">LEAVE A MESSAGE</div>
<div class="btn" style="left:482px;top:3847px;width:160px">SUBMIT <span class="arrow"><svg viewBox="0 0 10 10"><path d="M3 2l3 3-3 3" stroke="#7cc142" stroke-width="2" fill="none"/></svg></span></div>
<div class="cphone" style="left:677px;top:3854px"><span class="ph-icon" style="width:36px;height:36px"><svg viewBox="0 0 24 24"><path fill="#f5a623" d="M6.6 10.8a15 15 0 006.6 6.6l2.2-2.2a1 1 0 011-.25 11.4 11.4 0 003.6.57 1 1 0 011 1V20a1 1 0 01-1 1A17 17 0 013 4a1 1 0 011-1h3.5a1 1 0 011 1c0 1.25.2 2.45.57 3.6a1 1 0 01-.25 1z"/></svg></span>(555) 014-2739</div>
<div class="cphone" style="left:875px;top:3854px"><span class="ph-icon" style="width:36px;height:36px"><svg viewBox="0 0 24 24"><path fill="#f5a623" d="M6.6 10.8a15 15 0 006.6 6.6l2.2-2.2a1 1 0 011-.25 11.4 11.4 0 003.6.57 1 1 0 011 1V20a1 1 0 01-1 1A17 17 0 013 4a1 1 0 011-1h3.5a1 1 0 011 1c0 1.25.2 2.45.57 3.6a1 1 0 01-.25 1z"/></svg></span>(555) 019-9939</div>

<!-- news -->
<h2 class="sec-title" style="top:4008px">LATEST NEWS</h2>
<div class="sec-sub" style="top:4069px">READ OUR BLOG</div>
<div class="sec-line" style="top:4097px"></div>

<div class="post-img" style="left:120px;background:linear-gradient(140deg,#7a8a6a,#d45a2a 50%,#5a6a4a)" role="img" aria-label="Chainsaw among cut branches"></div>
<div class="post-img" style="left:443px;background:linear-gradient(140deg,#3f6a2a,#9ac06a 50%,#2f4a22)" role="img" aria-label="Gloved hand pruning a shrub"></div>
<div class="post-img" style="left:767px;background:linear-gradient(140deg,#3a6ab0,#e07a2a 45%,#c8a060 75%,#5a4a30)" role="img" aria-label="Chainsaw cutting a log"></div>

<div class="post-title" style="left:120px">LOREM IPSUM DOLOR SIT AMET CONSECTETUR ADI</div>
<div class="post-title" style="left:443px">LOREM IPSUM DOLOR SIT AMET CONSECTETUR ADI</div>
<div class="post-title" style="left:767px">LOREM IPSUM DOLOR SIT AMET CONSECTETUR ADI</div>

<div class="post-meta" style="left:120px"><span><b></b>Admin,</span><span><b></b>14 JUN 2024</span></div>
<div class="post-meta" style="left:443px"><span><b></b>Admin,</span><span><b></b>14 JUN 2024</span></div>
<div class="post-meta" style="left:767px"><span><b></b>Admin,</span><span><b></b>14 JUN 2024</span></div>

<div class="btn" style="left:120px;top:4545px;width:160px">VIEW MORE <span class="arrow"><svg viewBox="0 0 10 10"><path d="M3 2l3 3-3 3" stroke="#7cc142" stroke-width="2" fill="none"/></svg></span></div>
<div class="btn" style="left:443px;top:4545px;width:160px">VIEW MORE <span class="arrow"><svg viewBox="0 0 10 10"><path d="M3 2l3 3-3 3" stroke="#7cc142" stroke-width="2" fill="none"/></svg></span></div>
<div class="btn" style="left:767px;top:4545px;width:160px">VIEW MORE <span class="arrow"><svg viewBox="0 0 10 10"><path d="M3 2l3 3-3 3" stroke="#7cc142" stroke-width="2" fill="none"/></svg></span></div>

<!-- footer -->
<footer class="abs footer"></footer>
<div class="abs brand" style="left:120px;top:4808px">
  <span class="brand-mark"></span>
  <span class="brand-name" style="color:#fff">QUILLBY<br>TREE CARE</span>
</div>
<p class="abs" style="left:120px;top:4875px;width:310px;color:#fff;font-size:15px;line-height:27px">At Quillby Tree Care, we are more than just a tree service company, we are stewards of our beautiful trees.</p>
<div class="abs social footer-social" style="left:120px;top:4976px"><span></span><span></span><span></span></div>

<div class="f-head" style="left:555px">QUICK LINKS</div>
<ul class="f-list" style="left:555px"><li>Home</li><li>About</li><li>Services</li><li>Blog</li><li>Contact</li></ul>

<div class="f-head" style="left:810px">CONTACT INFORMATION</div>
<div class="f-contact" style="top:4838px"><span class="f-pin"><svg viewBox="0 0 24 24"><path fill="#fff" d="M12 2a7 7 0 00-7 7c0 5 7 13 7 13s7-8 7-13a7 7 0 00-7-7zm0 9.5A2.5 2.5 0 1112 6.5a2.5 2.5 0 010 5z"/></svg></span><span>Inventore veritatis et mani<br>quasi architecto</span></div>
<div class="f-contact" style="top:4912px"><span class="f-pin"><svg viewBox="0 0 24 24"><path fill="#fff" d="M6.6 10.8a15 15 0 006.6 6.6l2.2-2.2a1 1 0 011-.25 11.4 11.4 0 003.6.57 1 1 0 011 1V20a1 1 0 01-1 1A17 17 0 013 4a1 1 0 011-1h3.5a1 1 0 011 1c0 1.25.2 2.45.57 3.6a1 1 0 01-.25 1z"/></svg></span><span>Call us:<br>(555) 014-2739</span></div>
<div class="f-contact" style="top:4980px"><span class="f-pin"><svg viewBox="0 0 24 24"><path fill="#fff" d="M6.6 10.8a15 15 0 006.6 6.6l2.2-2.2a1 1 0 011-.25 11.4 11.4 0 003.6.57 1 1 0 011 1V20a1 1 0 01-1 1A17 17 0 013 4a1 1 0 011-1h3.5a1 1 0 011 1c0 1.25.2 2.45.57 3.6a1 1 0 01-.25 1z"/></svg></span><span>Call us:<br>(555) 019-9939</span></div>

<div class="abs" style="left:120px;top:5120px;width:958px;height:1px;background:#2c3529"></div>
<div class="abs" style="left:0;top:5150px;width:1200px;text-align:center;color:#fff;font-size:13px;font-weight:600">Copyright © 2024 QUILLBY Tree Care. All rights reserved.</div>

</body>
</html>
```